Ad design for a macarons brand

We are a dessert brand with one product line: macarons. Our products delight. Every bite is a dream!

We are launching a new product and would like to lunch a small tactical campaign for the product to boost sales.

The new macron is mango ganache and the middle a mix of sour mango and yuzu (https://www.plumvarell.com/about-the-fruit-584302).

Here are some images we took of the new macaron
https://www.fennlocker.com/sh/qrtwpzhkvbmls/AAFJtRWD-nxPlkhQZ7CeW4DLp?dl=0

I attach the brand guideline document.

Required sizes

1080 x 1350
1080 x 1920

```html
<!DOCTYPE html>
<html lang="en">
<head>
<meta charset="utf-8">
<title>Mareval – Every Bite's a Dream</title>
<link rel="stylesheet" href="https://fonts.googleapis.com/css2?family=Playfair+Display:wght@400;500&display=swap">
<style>
  :root{
    --cream:#f9cf7f;
    --peach:#f2ac72;
    --coral:#e88a6b;
    --ink:#141210;
    --blue:#5c9be0;
    --white:#ffffff;
    --shell:#e9a446;
    --shell-deep:#d98a34;
    --filling:#f2c234;
    --paper:#f1e6d2;
    --mango-deep:#ec9a22;
    --mango-light:#f9cc3c;
    --leaf:#8cbf4a;
  }
  *{margin:0;padding:0;box-sizing:border-box}
  html,body{width:675px;height:1200px;overflow:hidden;background:var(--cream)}
  .ad{position:relative;width:675px;height:1200px;overflow:hidden;background:var(--cream);font-family:"Playfair Display",serif}
  .backdrop{position:absolute;inset:0;width:675px;height:1200px}
  .brand{position:absolute;left:26px;top:34px;font-size:46px;font-weight:400;color:var(--ink);letter-spacing:-1px;line-height:1}
  .headline{position:absolute;left:0;width:675px;top:214px;text-align:center;font-size:68px;font-weight:400;line-height:70px;color:var(--ink);letter-spacing:-1px}
  .socials{position:absolute;left:16px;top:1132px;display:flex;gap:21px}
  .social{width:44px;height:44px;border-radius:50%;background:var(--white);display:flex;align-items:center;justify-content:center;font-size:10px;color:var(--ink);font-family:"Playfair Display",serif}
</style>
</head>
<body>
<main class="ad">
  <svg class="backdrop" viewBox="0 0 675 1200">
    <defs>
      <linearGradient id="blobWarm" x1="0" y1="0" x2="0" y2="1">
        <stop offset="0" stop-color="var(--peach)" stop-opacity=".75"/>
        <stop offset="1" stop-color="var(--coral)"/>
      </linearGradient>
      <linearGradient id="photoTone" x1="0" y1="0" x2="0" y2="1">
        <stop offset="0" stop-color="var(--mango-light)"/>
        <stop offset=".2" stop-color="var(--paper)"/>
        <stop offset=".38" stop-color="var(--shell)"/>
        <stop offset=".62" stop-color="var(--shell-deep)"/>
        <stop offset=".8" stop-color="var(--shell)"/>
        <stop offset="1" stop-color="#e4b77a"/>
      </linearGradient>
      <linearGradient id="mangoTone" x1="0" y1="0" x2="1" y2="1">
        <stop offset="0" stop-color="var(--mango-light)"/>
        <stop offset="1" stop-color="var(--mango-deep)"/>
      </linearGradient>
    </defs>

    <path d="M0 100 C90 130 160 220 165 300 C170 380 120 420 90 470 C60 520 40 600 0 630 Z" fill="url(#blobWarm)"/>
    <path d="M450 0 H675 V180 C620 185 560 180 510 150 C450 115 430 50 450 0 Z" fill="var(--peach)" opacity=".8"/>
    <path d="M675 270 C610 300 560 370 560 450 C560 520 610 560 675 590 Z" fill="url(#blobWarm)"/>
    <path d="M0 900 C70 930 120 980 140 1020 C170 1060 240 1070 270 1100 C300 1130 310 1170 305 1200 H0 Z" fill="url(#blobWarm)"/>
    <path d="M675 840 C640 880 650 940 660 1000 L675 1200 Z" fill="url(#blobWarm)"/>

    <path role="img" aria-label="Close-up photo of mango macarons with yellow mango and yuzu filling, stacked on a table with fresh mango pieces behind"
      d="M205 445 C260 410 330 405 385 425 C445 445 490 490 540 520 C600 555 665 600 662 690 C660 770 620 820 560 870 C500 920 430 960 340 985 C260 998 180 975 120 900 C85 850 72 780 72 700 C72 610 110 505 205 445 Z"
      fill="url(#photoTone)"/>

    <path role="img" aria-label="Photo of two ripe mangoes, one cut in a hedgehog pattern"
      d="M262 1085 C258 1035 300 995 360 975 C400 962 440 945 480 925 C540 900 620 905 658 955 C685 995 676 1070 650 1120 C625 1165 585 1192 540 1188 C500 1185 470 1160 440 1150 C380 1150 320 1148 285 1128 C270 1118 263 1102 262 1085 Z"
      fill="url(#mangoTone)"/>

    <g fill="none" stroke="var(--blue)" stroke-width="4" stroke-linecap="round" stroke-linejoin="round">
      <polyline points="160,375 170,387 158,399 170,411 158,423 170,435 164,441"/>
      <polyline points="520,382 530,394 518,406 530,418 518,430 530,442 524,449"/>
      <path d="M608 519 H630 M619 508 V530" stroke-width="6"/>
    </g>
    <g fill="var(--blue)">
      <g id="dotRowR">
        <circle cx="617" cy="220" r="1.8"/><circle cx="633" cy="220" r="1.8"/><circle cx="649" cy="220" r="1.8"/><circle cx="665" cy="220" r="1.8"/>
      </g>
      <use href="#dotRowR" y="16"/><use href="#dotRowR" y="32"/><use href="#dotRowR" y="48"/><use href="#dotRowR" y="64"/><use href="#dotRowR" y="80"/><use href="#dotRowR" y="96"/><use href="#dotRowR" y="112"/>
      <g id="dotRowL">
        <circle cx="35" cy="714" r="1.8"/><circle cx="51" cy="714" r="1.8"/><circle cx="67" cy="714" r="1.8"/><circle cx="83" cy="714" r="1.8"/>
      </g>
      <use href="#dotRowL" y="16"/><use href="#dotRowL" y="32"/><use href="#dotRowL" y="48"/><use href="#dotRowL" y="64"/><use href="#dotRowL" y="80"/><use href="#dotRowL" y="96"/><use href="#dotRowL" y="112"/>
    </g>
    <g stroke="var(--blue)" stroke-width="4">
      <line x1="30" y1="0" x2="40" y2="12"/><line x1="42" y1="0" x2="52" y2="12"/><line x1="54" y1="0" x2="64" y2="12"/><line x1="66" y1="0" x2="76" y2="12"/><line x1="78" y1="0" x2="86" y2="10"/>
    </g>
  </svg>

  <div class="brand">MAREVAL</div>

  <h1 class="headline">EVERY BITE’S A<br>DREAM</h1>

  <nav class="socials">
    <span class="social">Pica</span>
    <span class="social">Folio</span>
    <span class="social">Chirp</span>
    <span class="social">Talky</span>
  </nav>
</main>
</body>
</html>
```